依頼詳細
地元の方々に会社のことを知っていただきたく、富山市の北部エリアでチラシを配布しようと考えております。
記載項目
社名:合同会社ほたるいし不動産
住所:富山市西早瀬四丁目3番12号
TEL:076-555-0182
キャッチコピー:富山市北部の不動産売買ならほたるいし不動産!

サイズ
A4
ページ数
片面
希望イメージ
シンプル 複雑
単色 カラフル
暗い 明るい
日常 高級
遊び心 厳粛
未来的 伝統的
女性的 男性的
希望する色
黄・オレンジ系
納品ファイル
補足説明

```html
<!DOCTYPE html>
<html lang="ja">
<head>
<meta charset="utf-8">
<title>ほたるいし不動産 チラシ</title>
<link rel="stylesheet" href="https://fonts.googleapis.com/css2?family=M+PLUS+Rounded+1c:wght@500;700;800&family=Noto+Sans+JP:wght@400;500;700&family=Quicksand:wght@500;600&display=swap">
<style>
  :root {
    --orange: #e98a2b;
    --orange-deep: #e06f14;
    --cream: #fdf1c4;
    --cream-light: #fff8dc;
    --brown: #4b2b14;
    --yellow: #f8d640;
    --green: #7dbb3c;
    --green-light: #a9d36a;
    --honey: #f3bd3e;
    --white: #ffffff;
    --ink: #3a2414;
  }
  * { box-sizing: border-box; margin: 0; padding: 0; }
  html, body { width: 846px; height: 1200px; overflow: hidden; background: var(--orange); }
  .flyer {
    position: relative; width: 846px; height: 1200px; overflow: hidden;
    background: var(--orange);
    font-family: "Noto Sans JP", sans-serif; color: var(--ink);
  }
  .clover-wreath {
    position: absolute; left: 48px; top: 20px; width: 750px; height: 750px; border-radius: 50%;
    background: radial-gradient(circle, transparent 0 41%, var(--green-light) 42%, var(--green) 47%, var(--green-light) 49.5%, transparent 50%);
    -webkit-mask-image: conic-gradient(from 140deg, transparent 0 78deg, #000 78deg);
            mask-image: conic-gradient(from 140deg, transparent 0 78deg, #000 78deg);
  }
  .hero-circle {
    position: absolute; left: 110px; top: 82px; width: 626px; height: 626px;
    border-radius: 50%;
    background: radial-gradient(circle, var(--cream-light) 0%, var(--cream) 75%, #f8e3a0 100%);
  }
  .bee {
    position: absolute; border-radius: 50%;
    background: radial-gradient(circle at 40% 40%, #fbe38a, var(--honey));
  }
  .honeycomb {
    position: absolute; border-radius: 14px;
    background: linear-gradient(135deg, #f6cd55, #eaa52c);
  }
  .tagline {
    position: absolute; top: 186px; left: 0; width: 100%; text-align: center;
    font-family: "M PLUS Rounded 1c", sans-serif; font-weight: 700; font-size: 30px;
    color: var(--brown); letter-spacing: 1px;
  }
  .brand-title {
    position: absolute; top: 236px; left: 0; width: 100%; text-align: center;
    font-family: "M PLUS Rounded 1c", sans-serif; font-weight: 800; font-size: 100px;
    line-height: 1.18; color: var(--orange-deep); letter-spacing: 4px;
  }
  .brand-latin {
    position: absolute; top: 508px; left: 0; width: 100%; text-align: center;
    font-family: "Quicksand", sans-serif; font-weight: 600; color: var(--brown);
    line-height: 1.15;
  }
  .brand-latin .latin-name { display: block; font-size: 42px; letter-spacing: 4px; }
  .brand-latin .latin-sub { display: block; font-size: 38px; font-weight: 500; }
  .intro-box {
    position: absolute; left: 52px; top: 655px; width: 486px; height: 400px;
    background: var(--brown); border-radius: 16px; padding: 26px 26px;
    color: var(--white); font-size: 22px; font-weight: 500;
  }
  .intro-box p {
    line-height: 1.2; padding: 13px 0; border-bottom: 2px dashed rgba(255,255,255,.45);
    white-space: nowrap;
  }
  .intro-box p:last-child { border-bottom: none; }
  .intro-box .highlight {
    display: inline-block; background: var(--white); color: var(--orange-deep);
    font-weight: 700; font-size: 27px; padding: 2px 8px; border-radius: 4px;
  }
  .intro-box .yellow { color: var(--yellow); }
  .speech { position: absolute; left: 610px; top: 612px; width: 222px; height: 156px; }
  .speech svg { position: absolute; inset: 0; }
  .speech p {
    position: absolute; inset: 0 0 16px; display: flex; flex-direction: column;
    justify-content: center; align-items: center; text-align: center;
    font-size: 19px; font-weight: 700; line-height: 1.5; color: var(--ink);
  }
  .staff-photo {
    position: absolute; left: 548px; top: 775px; width: 282px; height: 339px;
    background: linear-gradient(180deg, #f0a650 0%, #8a6a55 55%, #3e3f4a 100%);
  }
  .staff-caption {
    position: absolute; left: 548px; top: 1062px; width: 170px; text-align: center;
    font-size: 13px; line-height: 1.35; color: var(--white); font-weight: 500;
  }
  .footer {
    position: absolute; left: 0; bottom: 0; width: 100%; height: 86px;
    background: var(--white); display: flex; align-items: center;
    justify-content: space-between; padding: 0 34px 0 40px;
  }
  .company .company-name { font-size: 26px; font-weight: 700; color: var(--ink); }
  .company .address { font-size: 21px; font-weight: 500; color: var(--ink); margin-top: 2px; }
  .contact { text-align: right; }
  .contact .tel { font-size: 46px; font-weight: 700; color: var(--orange-deep); line-height: 1; letter-spacing: 1px; }
  .contact .tel small { font-size: 30px; margin-right: 6px; }
  .contact .hours { font-size: 14px; color: var(--ink); margin-top: 6px; }
</style>
</head>
<body>
<main class="flyer">
  <div class="clover-wreath" role="img" aria-label="円を囲むクローバーのリース"></div>
  <div class="hero-circle"></div>

  <div class="bee" role="img" aria-label="ミツバチのイラスト" style="left:232px;top:60px;width:74px;height:66px"></div>
  <div class="bee" role="img" aria-label="ミツバチのイラスト" style="left:606px;top:118px;width:70px;height:62px"></div>
  <div class="bee" role="img" aria-label="ハチミツ壺とミツバチのイラスト" style="left:126px;top:500px;width:92px;height:100px"></div>
  <div class="bee" role="img" aria-label="ミツバチのイラスト" style="left:666px;top:486px;width:70px;height:62px"></div>
  <div class="honeycomb" role="img" aria-label="ハチの巣の模様" style="left:0;top:500px;width:70px;height:124px"></div>
  <div class="honeycomb" role="img" aria-label="ハチの巣の模様" style="left:776px;top:520px;width:70px;height:124px"></div>

  <p class="tagline">富山市北部の不動産売買なら</p>
  <h1 class="brand-title">ほたるいし<br>不動産</h1>
  <p class="brand-latin"><span class="latin-name">HOTARUISHI</span><span class="latin-sub">real estate</span></p>

  <section class="intro-box">
    <p>富山市北部エリアで活動中の</p>
    <p><span class="highlight">ほたるいし不動産</span>です！</p>
    <p>不動産売買を中心に行っています。</p>
    <p><span class="yellow">相続</span>のご相談から<span class="yellow">不動産売却</span>など</p>
    <p>ご依頼承っております。</p>
    <p>お気軽にお問い合わせください。</p>
  </section>

  <div class="staff-photo" role="img" aria-label="スーツ姿のスタッフの写真"></div>
  <p class="staff-caption">ほたるいし不動産<br>川端 健</p>

  <div class="speech">
    <svg viewBox="0 0 222 156" width="222" height="156" aria-hidden="true">
      <ellipse cx="111" cy="70" rx="108" ry="66" fill="#ffffff"/>
      <path d="M70 124 L52 154 L98 132 Z" fill="#ffffff"/>
    </svg>
    <p>相続診断士の<br>資格保持者が<br>ご相談にのります</p>
  </div>

  <footer class="footer">
    <div class="company">
      <p class="company-name">合同会社ほたるいし不動産</p>
      <p class="address">富山市西早瀬四丁目3番12号</p>
    </div>
    <div class="contact">
      <p class="tel"><small>TEL</small>076-555-0182</p>
      <p class="hours">受付時間：10：00～18：00　定休日：毎週○曜日</p>
    </div>
  </footer>
</main>
</body>
</html>
```